Book/Ebook Cover design for teen girls on purity/modesty
The Shape of Stillness: A Young Woman's Map to Quiet Strength
Book/Ebook Cover design for teen girls on purity/modesty - Books
Creative Brief
This book will be marketed to teenage girls, female family members like moms, grandmothers, aunts, etc., youth pastors, pastors, etc. I want a clean, fresh yet feminine look and feel. I envision an ornate mirror (handheld or otherwise) with the word "purity" being reflected on the mirror from the title. That is what's in my mind but I'm open to other ideas. Colors I like: aqua blue, bright green, and white.
Books
Feminine, fresh, charming, clean, modern.
This book will be published through Inkvale Press and Pagebrook. Full Bleed needed for the hard copy book. No less that 300 DPI. Need to know the basics about trim, margin, etc for book covers. RGB preferred.
tmerrow tmerrow
To Designers, I've uploaded an updated bio for myself for the back cover. I'll be choosing a winner very soon! Thank you so much for all your designs and hard work. I really appreciate it! Colette
FRIENDLY NOTE TO ALL DESIGNERS! Thanks for all your designs so far. Please do not include images of girls. I want the cover to draw girls from all backgrounds and an image of a girl whose skin color, hair and clothing makes a statement to one particular kind of girl. I want to make a statement to as many different kinds of girls as possible as the message is for them all. Also author name should either read "Colette J. Merrow" or "Colette Merrow". That's all for now. Please let me know how else I can help.
To all designers, Thanks for your willingness to create a design for my book! Size of book is 5.5X8.5. I'll need front and back cover designed. The mirror idea (described in the brief) is just something in my head. It can be pulled off believe but I'm also open to whatever fresh, clean and modern ideas you may have! Thanks again, tmerrow
Hi designers, It was brought to my attention that possibly the reason I haven't been getting many designers to commit is because this project isn't marked "guaranteed". I was under the impression that all projects were guaranteed. I do intend on picking a winner! I will call CS first thing Monday to see if I can change the project to read that it indeed is guaranteed. Until then, thanks so much for your submissions! I'm looking forward to picking one of your designs!
Dear designers, I would like to see some minimalistic designs. Simplistic but charming and feminine with a modern touch. Maybe the background the aqua blue color I like with a cute sketch of a mirror in white or with "purity" in a script font of some sort in the mirror. I'm not sure I'm going to like any of the random background kind of pictures. Thanks so much everyone. Tmerrow
Designers, The text for the back cover has not also been uploaded. Thanks!
To all designers, Thanks ahead of time for taking time to work on this project! I'm super excited to see what you all come up with. Please don't hesitate to ask questions or make suggestions. I have uploaded my head shot to use for the back cover. I am putting the finishing touches on the text for the back cover as well and will have that uploaded tonight or tomorrow. I'm not sure about how the ISBN will be printed on the book. Getting details on that as well. Thanks again! tmerrow

```html
<!DOCTYPE html>
<html lang="en">
<head>
<meta charset="utf-8">
<title>The Shape of Stillness — Cover Spread</title>
<link href="https://fonts.googleapis.com/css2?family=Great+Vibes&family=Lato:ital,wght@0,300;0,400;0,700;1,300;1,400;1,700&family=Oswald:wght@400;500&display=swap" rel="stylesheet">
<style>
  :root {
    --sky-light: #f3fcfe;
    --sky-mid: #d6f1f8;
    --sky-deep: #b9e6f2;
    --spine: #e6f7fb;
    --ink-grey: #8a8f93;
    --ink-script: #9a9fa3;
    --ink-dark: #4a4f53;
    --ink-blue: #2f6f86;
    --white: #ffffff;
  }
  * { margin: 0; padding: 0; box-sizing: border-box; }
  html, body { width: 1200px; height: 850px; overflow: hidden; background: var(--white); }
  .spread {
    position: relative;
    width: 1200px; height: 850px;
    background: linear-gradient(170deg, var(--sky-light) 0%, var(--sky-mid) 55%, var(--sky-deep) 100%);
    font-family: "Lato", sans-serif;
    color: var(--ink-dark);
    overflow: hidden;
  }

  /* Back cover */
  .back { position: absolute; left: 0; top: 0; width: 552px; height: 850px; }
  .back-blooms { position: absolute; left: 360px; top: 10px; width: 190px; height: 170px; }
  .back-heading { font-weight: 300; color: var(--ink-grey); }
  .back-heading span { position: absolute; white-space: nowrap; }
  .back-heading .lead { left: 30px; top: 20px; font-style: italic; font-size: 28px; }
  .back-heading .script { left: 105px; top: 52px; font-family: "Great Vibes", cursive; font-size: 88px; line-height: 1; color: var(--ink-script); }
  .back-heading .tail { left: 355px; top: 150px; font-style: italic; font-size: 26px; }
  .blurb { position: absolute; left: 36px; top: 222px; width: 440px; font-size: 11.5px; line-height: 1.45; }
  .promise-title { position: absolute; left: 76px; top: 428px; font-size: 13px; font-style: italic; font-weight: 700; color: var(--ink-blue); }
  .promises { position: absolute; left: 110px; top: 470px; width: 350px; list-style: none; }
  .promises li { position: relative; font-size: 11.5px; line-height: 1.45; margin-bottom: 22px; padding-left: 24px; }
  .promises li::before { content: ""; position: absolute; left: 0; top: 4px; width: 8px; height: 8px; border-radius: 50%; background: var(--ink-dark); }
  .author-photo { position: absolute; left: 48px; top: 680px; width: 84px; height: 92px; background: linear-gradient(160deg, #5b5b5b, #1f1f1f); }
  .bio { position: absolute; left: 142px; top: 680px; width: 165px; font-size: 8.5px; line-height: 1.35; }
  .bio .bio-name { display: block; }
  .isbn-box { position: absolute; left: 365px; top: 696px; width: 144px; height: 64px; background: var(--white); }

  /* Spine */
  .spine { position: absolute; left: 552px; top: 0; width: 60px; height: 850px; background: linear-gradient(90deg, var(--spine), var(--sky-light), var(--spine)); }
  .spine-text { position: absolute; left: 50%; transform: translateX(-50%); writing-mode: vertical-rl; white-space: nowrap; color: var(--ink-grey); }
  .spine-author { top: 36px; font-family: "Oswald", sans-serif; font-size: 17px; letter-spacing: 2px; }
  .spine-sub { top: 318px; font-size: 11px; font-style: italic; }
  .spine-title { top: 580px; font-size: 14px; font-weight: 300; }
  .spine-title .script { font-family: "Great Vibes", cursive; font-size: 30px; }

  /* Front cover */
  .front { position: absolute; left: 612px; top: 0; width: 588px; height: 850px; }
  .front-title { font-weight: 300; color: var(--ink-grey); }
  .front-title span { position: absolute; white-space: nowrap; }
  .front-title .pre { left: 330px; top: 108px; font-size: 19px; }
  .front-title .script { left: 120px; top: 128px; font-family: "Great Vibes", cursive; font-size: 104px; line-height: 1; color: var(--ink-script); }
  .front-title .sub { left: 0; width: 588px; text-align: center; top: 248px; font-size: 15px; font-style: italic; }
  .front-blooms { position: absolute; left: 20px; top: 300px; width: 568px; height: 420px; }
  .front-author { position: absolute; left: 100px; top: 730px; width: 410px; text-align: right; font-family: "Oswald", sans-serif; font-weight: 500; font-size: 33px; letter-spacing: 1px; color: var(--ink-grey); }
</style>
</head>
<body>
<div class="spread">

  <section class="back">
    <svg class="back-blooms" viewBox="0 0 190 170" role="img" aria-label="Faint outlined rose illustration">
      <defs>
        <radialGradient id="backBloom" cx="50%" cy="50%" r="50%">
          <stop offset="0%" stop-color="#ffffff" stop-opacity="0.7"/>
          <stop offset="100%" stop-color="#ffffff" stop-opacity="0"/>
        </radialGradient>
      </defs>
      <rect width="190" height="170" fill="url(#backBloom)"/>
    </svg>

    <h2 class="back-heading">
      <span class="lead">What does</span>
      <span class="script">Stillness</span>
      <span class="tail">look like?</span>
    </h2>

    <p class="blurb">Is it recognizable to the average teenage girl? Does she know that purity should be at the very foundation of her identity over makeup, short skirts, and finding a boyfriend? Purity carries an unpopular message in our culture, but the ignorance of purity could quite possibly be the greatest cause of the low self-esteem epidemic among teenage girls in our society. If a girl doesn't understand what kind of woman she was created to become, then chances are she will believe lies about herself from modern culture. As a result, throughout her life she will behave as if she's a much lesser being than her Creator meant her to be. She may even become sexually active early in an attempt to feel desired and accepted. It's time she learns that her true beauty radiates brightly from the inside out!</p>

    <h3 class="promise-title">The Shape of Stillness will:</h3>
    <ul class="promises">
      <li>Define what purity is from God's perspective…not the world's.</li>
      <li>Teach teenage girls Biblically about their true identity and purpose amid the lies from media and pop culture.</li>
      <li>Guide teenage girls to sexual purity through a deeper walk with their Creator.</li>
      <li>Help teenage girls overcome 5 major obstacles to living a lifestyle of purity.</li>
    </ul>

    <div class="author-photo" role="img" aria-label="Author headshot"></div>
    <p class="bio"><span class="bio-name">Colette Merrow</span>short bio goes here short bio goes here short bio goes here short bio goes here short bio goes here short bio goes here short bio goes here short bio goes here short bio goes here</p>
    <div class="isbn-box"></div>
  </section>

  <aside class="spine">
    <span class="spine-text spine-author">COLETTE J. MERROW</span>
    <span class="spine-text spine-sub">A Young Woman's Map to Quiet Strength</span>
    <span class="spine-text spine-title">The Shape of <span class="script">Stillness</span></span>
  </aside>

  <section class="front">
    <h1 class="front-title">
      <span class="pre">The Shape of</span>
      <span class="script">Stillness</span>
      <span class="sub">A Young Woman's Map to Quiet Strength</span>
    </h1>

    <svg class="front-blooms" viewBox="0 0 568 420" role="img" aria-label="Cluster of soft pale blue roses">
      <defs>
        <radialGradient id="bloomFill" cx="50%" cy="45%" r="55%">
          <stop offset="0%" stop-color="#e4f6fb"/>
          <stop offset="100%" stop-color="#a9dfee"/>
        </radialGradient>
      </defs>
      <circle cx="150" cy="160" r="95" fill="url(#bloomFill)" opacity="0.75"/>
      <circle cx="380" cy="120" r="80" fill="url(#bloomFill)" opacity="0.7"/>
      <circle cx="300" cy="290" r="120" fill="url(#bloomFill)" opacity="0.85"/>
      <circle cx="480" cy="280" r="75" fill="url(#bloomFill)" opacity="0.6"/>
    </svg>

    <p class="front-author">COLETTE J. MERROW</p>
  </section>

</div>
</body>
</html>
```